Project Sign for Construction Company

Site contractor needs a 4'x8' sign to place on construction sites for advertising. Our company builds the infrastructure for new housing developments. These sign will be posted on the road side to be viewed by passing cars. I want a clean and bold look and feel that resembles my company logo.

Font styles to use
Other font styles liked:
• Hypatia Sans Pro

Colors

Designer to choose colors to be used in the design.

Requirements
Must have
• 555-382-9146 | Info@MarlowPaving.example
• CUC 8047319
• www.MarlowPaving.example
• Services
• Road Construction
• Site Preparation & Excavation
• Underground Utilities
• Shoreline Restoration
Nice to have
• Now Hiring
• Pipe Layers
• Foremen
• Equipment Operators
Should not have
• Should not have stock picture images used in the design, focus on logo and geometric shapes

```html
<!DOCTYPE html>
<html lang="en">
<head>
<meta charset="utf-8">
<title>Marlow Paving – Site Sign</title>
<link rel="stylesheet" href="https://fonts.googleapis.com/css2?family=Encode+Sans+Condensed:wght@400;600;700&display=swap">
<style>
  :root {
    --backdrop: #232021;
    --paper: #ffffff;
    --brand-blue: #0656a4;
    --slate: #4a4a4c;
    --muted: #444444;
    --mark-tint-a: #e4ecf6;
    --mark-tint-b: #c9d8ea;
  }
  * { margin: 0; padding: 0; box-sizing: border-box; }
  html, body { width: 1200px; height: 1200px; overflow: hidden; background: var(--backdrop); }
  body { position: relative; font-family: "Encode Sans Condensed", "Arial Narrow", sans-serif; }

  .site-sign {
    position: absolute; left: 47px; top: 324px;
    width: 1105px; height: 553px;
    background: var(--paper); overflow: hidden;
  }
  .mascot-area {
    position: absolute; left: 0; top: 0; width: 363px; height: 406px;
    background: linear-gradient(160deg, var(--mark-tint-a), var(--mark-tint-b));
  }
  .license-number {
    position: absolute; right: 23px; top: 18px;
    font-size: 19px; font-weight: 400; color: var(--muted); letter-spacing: .5px;
  }
  .company-name {
    position: absolute; left: 433px; top: 62px; width: 607px;
    text-align: center; color: var(--brand-blue); font-weight: 700;
    line-height: 1;
  }
  .company-name .name-main { display: block; font-size: 122px; letter-spacing: 10px; }
  .company-name .name-sub { display: block; font-size: 38px; letter-spacing: 16px; margin-top: -6px; }

  .services {
    position: absolute; left: 420px; top: 238px; width: 650px;
    list-style: none; text-align: center;
    color: var(--brand-blue); font-size: 22px; font-weight: 600; line-height: 30px;
  }
  .services li { display: inline-block; margin: 0 10px; }
  .services li::before {
    content: ""; display: inline-block; width: 8px; height: 8px;
    background: var(--brand-blue); margin-right: 7px; vertical-align: 4px;
  }

  .hiring-badge {
    position: absolute; left: 599px; top: 321px; width: 262px; height: 40px;
    border-radius: 20px; background: var(--brand-blue); color: var(--paper);
    font-size: 31px; font-weight: 400; text-align: center; line-height: 40px;
  }
  .open-roles {
    position: absolute; left: 420px; top: 368px; width: 650px;
    text-align: center; color: var(--brand-blue);
    font-size: 22px; font-weight: 600;
  }
  .open-roles .divider { margin: 0 8px; }

  .contact-bar { position: absolute; left: 0; top: 463px; width: 1105px; height: 90px; }
  .contact-bar svg.bands { position: absolute; inset: 0; }
  .phone {
    position: absolute; left: 36px; top: 12px; height: 66px;
    display: flex; align-items: center; gap: 10px;
    color: var(--paper); font-size: 58px; font-weight: 700; letter-spacing: 1px;
  }
  .web-links {
    position: absolute; left: 500px; top: 22px; height: 68px; right: 24px;
    display: flex; align-items: center; justify-content: flex-end; gap: 28px;
    color: var(--paper); font-size: 21px; font-weight: 400; white-space: nowrap;
  }
  .web-links span { display: flex; align-items: center; gap: 8px; }
</style>
</head>
<body>
  <main class="site-sign">
    <div class="mascot-area" role="img" aria-label="Line illustration of the company's winged mascot in brand blue"></div>

    <p class="license-number">CUC 8047319</p>

    <h1 class="company-name">
      <span class="name-main">MARLOW</span>
      <span class="name-sub">PAVING</span>
    </h1>

    <ul class="services">
      <li>ROAD CONSTRUCTION</li>
      <li>SITE PREPARATION &amp; EXCAVATION</li>
      <li>UNDERGROUND UTILITIES</li>
      <li>SHORELINE RESTORATION</li>
    </ul>

    <div class="hiring-badge">NOW HIRING</div>
    <p class="open-roles">PIPE LAYERS<span class="divider">|</span>FOREMEN<span class="divider">|</span>EQUIPMENT OPERATORS</p>

    <footer class="contact-bar">
      <svg class="bands" width="1105" height="90" viewBox="0 0 1105 90">
        <polygon points="500,22 1105,22 1105,90 470,90" fill="var(--slate)"/>
        <polygon points="0,0 515,0 471,90 0,90" fill="var(--brand-blue)"/>
      </svg>
      <div class="phone">
        <svg width="48" height="48" viewBox="0 0 48 48" aria-hidden="true">
          <path d="M10 6c2-1 4 0 5 2l4 7c1 2 0 3-1 4l-3 2c2 5 6 9 11 11l2-3c1-1 2-2 4-1l7 4c2 1 3 3 2 5l-2 4c-1 2-3 3-5 3C18 43 5 30 5 14c0-2 1-4 3-5z" fill="var(--paper)"/>
          <path d="M27 13a9 9 0 0 1 8 8M28 6a16 16 0 0 1 14 14M29 0a22 22 0 0 1 19 19" stroke="var(--paper)" stroke-width="3" fill="none" stroke-linecap="round"/>
        </svg>
        555-382-9146
      </div>
      <div class="web-links">
        <span>
          <svg width="22" height="18" viewBox="0 0 22 18" aria-hidden="true">
            <rect x="1" y="3" width="20" height="14" fill="none" stroke="var(--paper)" stroke-width="1.6"/>
            <path d="M1 17l8-7M21 17l-8-7M1 3l10 8 10-8" fill="none" stroke="var(--paper)" stroke-width="1.6"/>
          </svg>
          Info@MarlowPaving.example
        </span>
        <span>
          <svg width="22" height="22" viewBox="0 0 22 22" aria-hidden="true">
            <circle cx="11" cy="11" r="9.5" fill="none" stroke="var(--paper)" stroke-width="1.4"/>
            <ellipse cx="11" cy="11" rx="4" ry="9.5" fill="none" stroke="var(--paper)" stroke-width="1.4"/>
            <path d="M1.5 11h19M3 6h16M3 16h16" stroke="var(--paper)" stroke-width="1.4"/>
          </svg>
          www.MarlowPaving.example
        </span>
      </div>
    </footer>
  </main>
</body>
</html>
```